I need a Label design for my tavin 58 kombucha brand that is launching soon

I want a label to go on my tavin 58 kombucha bottle.
I have a logo image uploaded in the files but I am open to changes to this logo or even a completely New one if you think you can do better. This logo is based on the idea of an s-shaped naga. I particularly like the nagas from temples in luang prabang.
I also want to include the slogan - dare to be delicious.
The label should be some kind of oval at 80mm high by 70mm wide.
The label will go on a clear glass bottle. The kombucha will be visible and comes in different shades of red,yellow and purple.
The word kombucha should be clearly visible.
i want a very colorful, playful label. I'm very keen to see your ideas and I want something original.
Fermented foods and beverages

```html
<!DOCTYPE html>
<html lang="en">
<head>
<meta charset="utf-8">
<title>tavin 58 Kombucha – Label Range</title>
<link href="https://fonts.googleapis.com/css2?family=Roboto+Condensed:wght@300;700&display=swap" rel="stylesheet">
<style>
  :root {
    --paper: #ffffff;
    --sage: #8fc1b0;
    --plum: #5b3a8a;
    --coral: #d0625e;
    --teal: #25b5bb;
    --navy: #1e3557;
    --white: #ffffff;
  }
  html, body {
    margin: 0;
    padding: 0;
    width: 946px;
    height: 1200px;
    overflow: hidden;
    background: var(--paper);
  }
  .label-range {
    width: 946px;
    height: 1200px;
    display: flex;
    align-items: center;
    justify-content: center;
    gap: 36px;
  }
  .label {
    width: 256px;
    height: 296px;
    display: block;
  }
  .label--plum { --outer: var(--sage);  --ring: var(--plum); --tone-a: var(--sage);  --tone-b: var(--plum);  --cap-text: var(--plum); }
  .label--teal { --outer: var(--coral); --ring: var(--teal); --tone-a: var(--teal);  --tone-b: var(--coral); --cap-text: var(--coral); }
  .label--navy { --outer: var(--navy);  --ring: var(--navy); --tone-a: var(--coral); --tone-b: var(--navy);  --cap-text: var(--navy); }

  .label__outer { fill: var(--outer); }
  .label__ring  { fill: var(--ring); }
  .tone-a { stop-color: var(--tone-a); }
  .tone-b { stop-color: var(--tone-b); }
  .label__cap { fill: var(--white); }
  .label__category {
    fill: var(--cap-text);
    font-family: "Roboto Condensed", sans-serif;
    font-weight: 700;
    font-size: 21px;
  }
  .label__slogan {
    fill: var(--white);
    font-family: "Roboto Condensed", sans-serif;
    font-weight: 700;
    text-transform: uppercase;
  }
  .label__brand {
    fill: var(--white);
    font-family: "Roboto Condensed", sans-serif;
    font-weight: 300;
    font-size: 30px;
  }
  .label__brand-mark {
    fill: none;
    stroke: var(--white);
    stroke-width: 2.5;
  }
</style>
</head>
<body>
<main class="label-range">

  <svg class="label label--plum" viewBox="0 0 280 320" role="img" aria-label="tavin 58 Kombucha label, purple and sage">
    <defs>
      <clipPath id="inner-plum"><ellipse cx="140" cy="160" rx="122" ry="142"/></clipPath>
      <linearGradient id="field-plum" x1="0" y1="0" x2="1" y2="1">
        <stop offset="0" class="tone-a"/><stop offset="1" class="tone-b"/>
      </linearGradient>
    </defs>
    <ellipse class="label__outer" cx="140" cy="160" rx="139" ry="159"/>
    <ellipse class="label__ring" cx="140" cy="160" rx="131" ry="151"/>
    <g clip-path="url(#inner-plum)">
      <rect fill="url(#field-plum)" x="0" y="0" width="280" height="320" role="img" aria-label="diagonal stripe pattern in sage and purple"/>
      <rect class="label__cap" x="0" y="0" width="280" height="48"/>
    </g>
    <text class="label__category" x="140" y="39" text-anchor="middle">Kombucha</text>
    <text class="label__slogan" x="140" y="104" font-size="46" text-anchor="middle">Dare</text>
    <text class="label__slogan" x="140" y="134" font-size="22" text-anchor="middle">to be</text>
    <text class="label__slogan" x="140" y="184" font-size="50" text-anchor="middle">delicious</text>
    <circle class="label__brand-mark" cx="78" cy="240" r="10"/>
    <text class="label__brand" x="150" y="251" text-anchor="middle">tavin 58</text>
  </svg>

  <svg class="label label--teal" viewBox="0 0 280 320" role="img" aria-label="tavin 58 Kombucha label, teal and coral">
    <defs>
      <clipPath id="inner-teal"><ellipse cx="140" cy="160" rx="122" ry="142"/></clipPath>
      <linearGradient id="field-teal" x1="0" y1="0" x2="1" y2="1">
        <stop offset="0" class="tone-a"/><stop offset="1" class="tone-b"/>
      </linearGradient>
    </defs>
    <ellipse class="label__outer" cx="140" cy="160" rx="139" ry="159"/>
    <ellipse class="label__ring" cx="140" cy="160" rx="131" ry="151"/>
    <g clip-path="url(#inner-teal)">
      <rect fill="url(#field-teal)" x="0" y="0" width="280" height="320" role="img" aria-label="diagonal stripe pattern in teal and coral"/>
      <rect class="label__cap" x="0" y="0" width="280" height="48"/>
    </g>
    <text class="label__category" x="140" y="39" text-anchor="middle">Kombucha</text>
    <text class="label__slogan" x="140" y="104" font-size="46" text-anchor="middle">Dare</text>
    <text class="label__slogan" x="140" y="134" font-size="22" text-anchor="middle">to be</text>
    <text class="label__slogan" x="140" y="184" font-size="50" text-anchor="middle">delicious</text>
    <circle class="label__brand-mark" cx="78" cy="240" r="10"/>
    <text class="label__brand" x="150" y="251" text-anchor="middle">tavin 58</text>
  </svg>

  <svg class="label label--navy" viewBox="0 0 280 320" role="img" aria-label="tavin 58 Kombucha label, navy and coral">
    <defs>
      <clipPath id="inner-navy"><ellipse cx="140" cy="160" rx="122" ry="142"/></clipPath>
      <linearGradient id="field-navy" x1="0" y1="0" x2="1" y2="1">
        <stop offset="0" class="tone-a"/><stop offset="1" class="tone-b"/>
      </linearGradient>
    </defs>
    <ellipse class="label__outer" cx="140" cy="160" rx="139" ry="159"/>
    <ellipse class="label__ring" cx="140" cy="160" rx="131" ry="151"/>
    <g clip-path="url(#inner-navy)">
      <rect fill="url(#field-navy)" x="0" y="0" width="280" height="320" role="img" aria-label="diagonal stripe pattern in coral and navy"/>
      <rect class="label__cap" x="0" y="0" width="280" height="48"/>
    </g>
    <text class="label__category" x="140" y="39" text-anchor="middle">Kombucha</text>
    <text class="label__slogan" x="140" y="104" font-size="46" text-anchor="middle">Dare</text>
    <text class="label__slogan" x="140" y="134" font-size="22" text-anchor="middle">to be</text>
    <text class="label__slogan" x="140" y="184" font-size="50" text-anchor="middle">delicious</text>
    <circle class="label__brand-mark" cx="78" cy="240" r="10"/>
    <text class="label__brand" x="150" y="251" text-anchor="middle">tavin 58</text>
  </svg>

</main>
</body>
</html>
```